Professional Document Wallet Design - Corporate Presentation Folder Design

Corporate Presentation Folder is known as a Document Wallet in Ireland.

This listing is for a design of a product called 'Document Wallets' - design for both inside and out. An example of the finished product is attached - 'preview document wallet.png'. This gives a clear example of what the document wallet looks like and for further details about this product you can visit this link.
http://www.presswerk-example.com/ie/group/double-gloss-lam-interlocking-presentation-folders
Attached "finish-image-1.jpg" gives an overview of the product outline as well as dimensions - also "preview document wallet"

'P10 template.indd' or 'P10 template.pdf' give the most detailed measurements of the product as these are the actual templates to be used in printing the product and therefore designs must be delivered on either of these.

Company Background

The client is a professional construction group and leads some of the largest construction jobs in the country for clients such as norvex, brado and tellura to name a few.
The brief is to design a document wallet both sides that reflects well on their corporate clients, shows off their existing branding clearly and highlights their strengths completely.
The clients current branding can be seen at this address http://dunphy.vantrelmedia.example/ but please be aware this website is still a work in progress.
An example of stationery styling liked by the client is found in the attached, Example of styling.pdf

Contents of the Design

As these document are a touch point for the company it is imperative that the following information is included.

1. The Company Logo
This must be clearly visible and the colouring around it enhance it's visibility. The logo should be to the fore and the design in no way should distract or detract attention from it.
2. Company Address and other contact details.
Address
Fernmount,
Kilcorrib,
Castlerea,
Co. Roscommon

T: 094 9270446
E: info@dunphygroup.example
W: www.dunphygroup.example

3. Some images should be included and can be found at
https://files.storebox.example/folderview?id=0X_QTrPmWjLsNnR7KdQ2bHcUeFa&usp=sharing
but stock images can be used if required to ensure the most professional look and feel for the project.

Printing
UV spot printing will be used on this printing and it is a requirement of the design to incorporate this into the finished article in some way. The document wallets are double sided so the same design should run throughout and consideration given to the user opening the wallet.
Updates

Target Market(s)

Professional corporate Clients

Industry/Entity Type

Product

Requirements
Must have
• Professional
• Striking
• Branding
• Logo
• Contact details
Nice to have
• A design surrounding the business card holder o the document wallet to enhance the area where the business card is held.

```html
<!DOCTYPE html>
<html lang="en">
<head>
<meta charset="utf-8">
<title>Document Wallet – Inside Spread</title>
<link rel="stylesheet" href="https://fonts.googleapis.com/css2?family=Arimo:wght@400;700&display=swap">
<style>
  :root {
    --navy: #302c6e;
    --royal: #2e2f8c;
    --heading-blue: #1f3fa8;
    --rule-blue: #25308f;
    --text-grey: #8a8a8a;
    --body-grey: #6d6d6d;
    --trim-line: #3a3a5a;
    --fold-red: #e0474f;
    --paper: #ffffff;
  }
  html, body {
    margin: 0;
    padding: 0;
    width: 1200px;
    height: 891px;
    overflow: hidden;
    background: var(--paper);
    font-family: "Arimo", Arial, sans-serif;
  }
  .artboard {
    position: relative;
    width: 1500px;
    height: 1114px;
    transform: scale(0.8);
    transform-origin: 0 0;
  }
  .dieline {
    position: absolute;
    inset: 0;
    width: 1500px;
    height: 1114px;
  }
  .panel-text { position: absolute; }
  .section-heading {
    margin: 0;
    color: var(--heading-blue);
    font-weight: 700;
    font-size: 11px;
    letter-spacing: 0.1px;
  }
  .client-list {
    left: 150px;
    top: 107px;
    width: 175px;
  }
  .client-list ul, .awards ul {
    list-style: none;
    margin: 0;
    padding: 0;
  }
  .client-list li {
    color: var(--text-grey);
    font-size: 8.6px;
    line-height: 16.2px;
  }
  .client-list .section-heading { margin-bottom: 1px; }
  .awards {
    left: 360px;
    top: 289px;
    width: 200px;
  }
  .awards .section-heading { margin-bottom: 14px; }
  .awards li {
    color: var(--text-grey);
    font-size: 8.4px;
    line-height: 20.9px;
  }
  .intro-copy {
    left: 148px;
    top: 450px;
    width: 163px;
  }
  .intro-copy p {
    margin: 0 0 11px;
    color: var(--body-grey);
    font-size: 5.6px;
    line-height: 11px;
    text-align: justify;
  }
  .photo {
    position: absolute;
    margin: 0;
  }
  .photo-skylight { left: 145px; top: 329px; width: 168px; height: 107px; background: linear-gradient(135deg, #c9dcef 0%, #6f9cc8 55%, #3e6a98 100%); }
  .photo-headquarters { left: 348px; top: 93px; width: 260px; height: 175px; background: linear-gradient(160deg, #d7dde2 0%, #7fa3c6 45%, #2f5a86 75%, #2e4a2c 100%); }
  .photo-ductwork { left: 348px; top: 508px; width: 166px; height: 123px; background: linear-gradient(120deg, #d9d2c3 0%, #9a9080 50%, #c9a35a 100%); }
  .photo-rooftop-unit { left: 148px; top: 651px; width: 166px; height: 124px; background: linear-gradient(180deg, #4e5f7e 0%, #b9bec4 45%, #5b5a57 100%); }
  .photo-rooftop-ducts { left: 348px; top: 651px; width: 166px; height: 124px; background: linear-gradient(180deg, #d4d6d8 0%, #a7a9ab 55%, #8c8d8e 100%); }
</style>
</head>
<body>
<div class="artboard">

  <svg class="dieline" viewBox="0 0 1500 1114" aria-hidden="true">
    <!-- crop and fold marks -->
    <g stroke="var(--trim-line)" stroke-width="1" fill="none">
      <line x1="98" y1="46" x2="98" y2="58"/>
      <line x1="84" y1="67" x2="90" y2="67"/>
      <line x1="84" y1="801" x2="90" y2="801"/>
      <line x1="98" y1="809" x2="98" y2="820"/>
    </g>
    <g stroke="var(--trim-line)" stroke-width="1" stroke-dasharray="2 2" fill="none">
      <line x1="627" y1="36" x2="627" y2="60"/>
      <line x1="1155" y1="36" x2="1155" y2="60"/>
      <line x1="1155" y1="905" x2="1155" y2="940"/>
    </g>

    <!-- pocket flap and cover sweep -->
    <path class="flap" fill="var(--navy)" stroke="#1b1a3d" stroke-width="1"
      d="M1130,60 L1160,60 C1300,60 1420,300 1443,802 L1163,802 L1163,905
         C1163,1000 1105,1050 1020,1050 C880,1050 720,955 648,807 L505,807
         C900,760 1150,600 1157,380 C1160,250 1150,150 1130,60 Z"/>

    <!-- spot-UV overlay blocks -->
    <path d="M1100,566 C1250,560 1360,575 1425,600 L1432,802 L1163,802 L1100,640 Z" fill="#2a2765" opacity="0.55"/>
    <rect x="1135" y="508" width="202" height="206" fill="#27265e" opacity="0.6"/>
    <rect x="1258" y="640" width="144" height="148" fill="#26255a" opacity="0.75"/>
    <rect class="card-holder" x="1224" y="603" width="139" height="142" fill="var(--royal)"/>

    <!-- business card slit arcs -->
    <g stroke="#111" stroke-width="1" fill="none">
      <path d="M1191,308 A22,22 0 0 0 1214,286"/>
      <path d="M1183,600 A88,88 0 0 0 1335,490"/>
      <path d="M1312,497 A26,26 0 0 1 1335,476"/>
    </g>

    <!-- inside trim edge -->
    <path d="M1130,60 L92,60 L92,807 L505,807" fill="none" stroke="var(--trim-line)" stroke-width="1"/>

    <!-- spine fold -->
    <line x1="627" y1="60" x2="627" y2="830" stroke="var(--fold-red)" stroke-width="1"/>
    <line x1="1157" y1="230" x2="1157" y2="380" stroke="var(--fold-red)" stroke-width="1" opacity="0.6"/>

    <!-- column rule -->
    <line x1="334" y1="83" x2="334" y2="615" stroke="var(--rule-blue)" stroke-width="2"/>
  </svg>

  <section class="panel-text client-list">
    <h2 class="section-heading">Featured Client List:</h2>
    <ul>
      <li>Chirographi neglegenter imputat.</li>
      <li>Apparatus bellis iocarisaetosus hecas.</li>
      <li>Medusa plane comiter conubium.</li>
      <li>Pompeii vix frugaliter vocificat ecast.</li>
      <li>Parsimonia matrimonii verecunde.</li>
      <li>Saetosus cathedras.</li>
      <li>Zothecas amputat umbraculi.</li>
      <li>Apparatus bellis conubium.</li>
      <li>Santet vix lascivius umbr aculi.</li>
      <li>Adlaudabilis agricolae catelli.</li>
      <li>Pompeii vix frugaliter vocificat ecast.</li>
    </ul>
  </section>

  <div class="photo photo-skylight" role="img" aria-label="Photo of a glass skylight roof against a blue sky"></div>

  <section class="panel-text intro-copy">
    <p>Caesar comiter insectat lascivius concubine. Pessimus perspicax saburre vix fortiter circumgrediet concubine, quamquam pessimus gulosus catelli vix frugaliter inset tat saburre. Parsim onia agricolae agnascor syrtes. Zothecas infeliciter am putat quadrupei.</p>
    <p>Quinqu ennalis fiducias corrumperet parsimonia catelli, et syrtes iocari trem ulus ossifragi, quod optimus adam laudabilis umbraculi senesceret catelli, quamquam bellus zothecas pessimus neglegenter adquireret adfabilis suis, etiam incredibiliter adlaudabilis concubine miscere gul sus oratori. Aquae Sulis celeriter con ubium.</p>
    <p>Pompeii Ossifragi circumgrediet Caesar, semper zothy cas plane lucide senesceret Medusa. Tremulus oratori frugaliter corrum peret saburre. Bellus syrtes vix comiter iocari ossifragi. Umbraculi suffra gant tremulus catelli, ut</p>
  </section>

  <div class="photo photo-headquarters" role="img" aria-label="Photo of a curved glass office headquarters with trees in the foreground"></div>

  <section class="panel-text awards">
    <h2 class="section-heading">Awards:</h2>
    <ul>
      <li>Quadrupei Fortiter</li>
      <li>Vocificat Medusa</li>
      <li>Semper</li>
      <li>Rures Verecunde</li>
      <li>Deciperet Saetosus</li>
      <li>Cathedras</li>
      <li>Zothecas amputat</li>
      <li>Umbraculi</li>
      <li>Apparatus Bellis</li>
    </ul>
  </section>

  <div class="photo photo-ductwork" role="img" aria-label="Photo of overhead ventilation ductwork in a building interior"></div>
  <div class="photo photo-rooftop-unit" role="img" aria-label="Photo of a rooftop air handling unit under a cloudy sky"></div>
  <div class="photo photo-rooftop-ducts" role="img" aria-label="Photo of galvanised steel ducting installed on a flat roof"></div>

</div>
</body>
</html>
```